Criação de Papelaria (6 itens) para Arquitetura
" Está sendo concluída a fábrica dos revestimentos, que será a responsável pela produção de todos os produtos 3D: painéis, murais, cobogós e imitações em pedra, em sua maioria fabricados em gesso especial, exclusivo da Ventra Relevo "

```html
<!DOCTYPE html>
<html lang="pt-BR">
<head>
<meta charset="utf-8">
<title>Assinatura de e-mail — Ventra Relevo</title>
<link rel="stylesheet" href="https://fonts.googleapis.com/css2?family=Roboto+Condensed:wght@400;700&display=swap">
<style>
  :root {
    --page-bg: #e9eaec;
    --navy-deep: #10175e;
    --navy-mid: #1f2f9a;
    --navy-light: #3346b8;
    --white: #ffffff;
    --text-soft: #dfe4ff;
    --strip-top: #f4f4f6;
    --strip-bottom: #b9bcc4;
  }
  * { margin: 0; padding: 0; box-sizing: border-box; }
  html, body {
    width: 1200px; height: 1200px; overflow: hidden;
    background: var(--page-bg);
    font-family: "Roboto Condensed", "Arial Narrow", sans-serif;
  }
  .signature {
    position: absolute; left: 77px; top: 509px;
    width: 1046px; height: 264px;
    border-radius: 8px; overflow: hidden;
    box-shadow: 0 6px 18px rgba(0,0,0,0.18);
  }
  .signature__band {
    position: absolute; inset: 0 0 24px 0;
    background:
      radial-gradient(ellipse 45% 90% at 92% 20%, rgba(90,120,230,0.45), transparent 70%),
      radial-gradient(ellipse 40% 80% at 15% 55%, rgba(70,95,210,0.35), transparent 70%),
      linear-gradient(180deg, var(--navy-mid) 0%, var(--navy-deep) 100%);
  }
  .signature__strip {
    position: absolute; left: 0; right: 0; bottom: 0; height: 24px;
    background: linear-gradient(180deg, var(--strip-top), var(--strip-bottom));
  }
  .brand {
    position: absolute; left: 30px; top: 0; height: 240px;
    display: flex; align-items: center; gap: 14px;
  }
  .brand__dot {
    width: 26px; height: 26px; border-radius: 50%;
    background: var(--white);
  }
  .brand__name {
    color: var(--white); font-weight: 700; font-size: 42px; letter-spacing: 0.5px;
  }
  .divider {
    position: absolute; left: 413px; top: 67px;
    width: 2px; height: 120px; background: rgba(255,255,255,0.85);
  }
  .person { position: absolute; left: 446px; top: 88px; color: var(--white); }
  .person__name { font-weight: 700; font-size: 30px; line-height: 1; margin-bottom: 8px; }
  .person__line {
    display: flex; align-items: center; gap: 8px;
    font-size: 17px; color: var(--text-soft); line-height: 24px;
  }
  .person__line svg { width: 16px; height: 16px; fill: var(--white); }
  .contacts { position: absolute; left: 700px; top: 50px; color: var(--text-soft); }
  .contact {
    position: absolute; left: 0; display: flex; align-items: center; gap: 10px;
    font-size: 12px; line-height: 13px; white-space: nowrap;
  }
  .contact__icon {
    width: 22px; height: 22px; border-radius: 50%; flex: none;
    background: var(--text-soft);
    display: flex; align-items: center; justify-content: center;
  }
  .contact__icon svg { width: 13px; height: 13px; fill: var(--navy-deep); }
  .contact--phone { top: 0; }
  .contact--web { top: 70px; }
  .contact--address { top: 120px; }
</style>
</head>
<body>
  <section class="signature" aria-label="Assinatura de e-mail Ventra Relevo">
    <div class="signature__band"></div>
    <div class="signature__strip"></div>

    <div class="brand">
      <span class="brand__dot"></span>
      <span class="brand__name">Ventra Relevo</span>
    </div>

    <div class="divider"></div>

    <div class="person">
      <p class="person__name">Nome Completo</p>
      <p class="person__line">
        <svg viewBox="0 0 16 16"><path d="M1 3h14v10H1z M2.5 4.2v.3L8 8.6l5.5-4.1v-.3z M2.5 6.3v5.2h11V6.3L8 10.4z" fill-rule="evenodd"/></svg>
        seuemail@provedor.com
      </p>
      <p class="person__line">
        <svg viewBox="0 0 16 16"><path d="M4 1.5l2.3 3-1.4 1.6c.9 1.9 2.4 3.5 4.4 4.6l1.6-1.4 3 2.3-1.5 2.4C7 13.8 2.2 9 1.6 3z"/></svg>
        [xx] xxxx-xxxx
      </p>
    </div>

    <div class="contacts">
      <div class="contact contact--phone">
        <span class="contact__icon"><svg viewBox="0 0 16 16"><path d="M4 1.5l2.3 3-1.4 1.6c.9 1.9 2.4 3.5 4.4 4.6l1.6-1.4 3 2.3-1.5 2.4C7 13.8 2.2 9 1.6 3z"/></svg></span>
        <span>[xx] xxxx-xxxx<br>[xx] xxxx-xxxx</span>
      </div>
      <div class="contact contact--web">
        <span class="contact__icon"><svg viewBox="0 0 16 16"><path d="M1 3h14v10H1z M2.5 4.2v.3L8 8.6l5.5-4.1v-.3z M2.5 6.3v5.2h11V6.3L8 10.4z" fill-rule="evenodd"/></svg></span>
        <span>www.seu-email.com</span>
      </div>
      <div class="contact contact--address">
        <span class="contact__icon"><svg viewBox="0 0 16 16"><path d="M8 1a5 5 0 0 0-5 5c0 3.6 5 9 5 9s5-5.4 5-9a5 5 0 0 0-5-5zm0 7a2 2 0 1 1 0-4 2 2 0 0 1 0 4z"/></svg></span>
        <span>R. Seu Endereço, 00 - Bairro<br>CEP 00000-000 - Cidade</span>
      </div>
    </div>
  </section>
</body>
</html>
```